QBTx 500mg CBD Tincture

We are rebranding and need new label ideas. I’m including our old label as reference to the bottle and the die lines.
Our company is called Marlow Fiber Company and we are a CBD company.

We would like a design for 1oz tincture bottle with a dropper. They are matte white with white tops. We have 2 flavors, peppermint and orange cream

I’ve uploaded the logo, colors and theme of the rebranding. We only want to use the Logos, no writing out of the company name. We are trying to shift to QBTx so that we can market more through the whole country.

We like clean and neat design. Elegant meets modern. Not cluttered. Our logo is new too so you can use that as an idea.

Requirements
Must have
• A neat and clean design. Something that is easily duplicated over other products over time.
Should not have
• My pro just must not have the company name written out. Only logo. No cannabis leaves.

```html
<!DOCTYPE html>
<html lang="en">
<head>
<meta charset="utf-8">
<title>QBTx CBD Tincture Labels</title>
<link href="https://fonts.googleapis.com/css2?family=Anton&family=Raleway:wght@400;500;600&family=Great+Vibes&display=swap" rel="stylesheet">
<style>
  :root {
    --page: #f1f1f2;
    --label-top: #d6d5d3;
    --orange: #d8713f;
    --orange-map: #e49b78;
    --teal: #74aba6;
    --teal-map: #5f9591;
    --ink: #262626;
    --ink-soft: #3a3a3a;
    --pill-dark: #222222;
    --white: #ffffff;
  }
  * { box-sizing: border-box; margin: 0; padding: 0; }
  html, body {
    width: 1013px;
    height: 1200px;
    overflow: hidden;
    background: var(--page);
  }
  .canvas {
    position: relative;
    width: 1013px;
    height: 1200px;
    display: flex;
    justify-content: center;
    align-items: center;
    gap: 40px;
  }
  .label {
    position: relative;
    width: 440px;
    height: 566px;
    overflow: hidden;
    background: var(--band);
  }
  .label--orange { --band: var(--orange); --map: var(--orange-map); }
  .label--teal { --band: var(--teal); --map: var(--teal-map); }

  .label__top {
    position: absolute;
    left: 0; top: 0;
    width: 100%;
    height: 162px;
    background: var(--label-top);
  }
  .brand-badge {
    position: absolute;
    left: 50%;
    top: 42px;
    width: 176px;
    height: 176px;
    margin-left: -88px;
    border-radius: 50%;
    background: var(--label-top);
    display: flex;
    align-items: center;
    justify-content: center;
  }
  .brand-name {
    font-family: "Raleway", sans-serif;
    font-weight: 500;
    font-size: 40px;
    letter-spacing: 2px;
    color: var(--ink);
  }
  .state-map {
    position: absolute;
    left: 340px;
    top: 368px;
    width: 72px;
    height: 188px;
    border-radius: 30px 20px 26px 40px;
    background: var(--map);
  }
  .product-title {
    position: absolute;
    left: 0; right: 0;
    top: 226px;
    text-align: center;
    font-family: "Anton", sans-serif;
    font-size: 112px;
    line-height: 1;
    color: var(--ink);
    letter-spacing: 1px;
  }
  .product-type {
    position: absolute;
    left: 0; right: 0;
    top: 340px;
    display: flex;
    justify-content: center;
    align-items: center;
    gap: 10px;
    font-family: "Raleway", sans-serif;
    font-weight: 600;
    font-size: 19px;
    color: var(--ink-soft);
  }
  .product-type::before,
  .product-type::after {
    content: "";
    width: 28px;
    height: 2px;
    background: var(--ink-soft);
  }
  .strength {
    position: absolute;
    left: 50%;
    top: 378px;
    width: 118px;
    height: 35px;
    margin-left: -64px;
    border: 1.5px solid var(--white);
    border-radius: 18px;
    display: flex;
    align-items: center;
    justify-content: center;
    font-family: "Raleway", sans-serif;
    font-weight: 600;
    font-size: 21px;
    color: var(--ink);
  }
  .flavor {
    position: absolute;
    left: 0; right: 0;
    top: 430px;
    text-align: center;
    font-family: "Great Vibes", cursive;
    font-size: 58px;
    line-height: 1;
    color: var(--ink-soft);
  }
  .spectrum {
    position: absolute;
    left: 0; right: 0;
    top: 498px;
    text-align: center;
    font-family: "Raleway", sans-serif;
    font-weight: 400;
    font-size: 17px;
    color: var(--ink-soft);
  }
  .net-weight {
    position: absolute;
    left: 50%;
    bottom: 0;
    width: 190px;
    height: 36px;
    margin-left: -99px;
    border-radius: 10px 10px 0 0;
    background: var(--pill-dark);
    display: flex;
    align-items: center;
    justify-content: center;
    font-family: "Raleway", sans-serif;
    font-size: 15px;
    color: var(--white);
  }
</style>
</head>
<body>
  <main class="canvas">
    <section class="label label--orange">
      <div class="label__top"></div>
      <div class="brand-badge"><span class="brand-name">QBTx</span></div>
      <div class="state-map" role="img" aria-label="Faint state outline map"></div>
      <h1 class="product-title">CBD OIL</h1>
      <p class="product-type">FULL SPECTRUM OIL</p>
      <p class="strength">500MG</p>
      <p class="flavor">Orange Cream</p>
      <p class="spectrum">BROAD SPECTRUM</p>
      <p class="net-weight">Net wt. 1fl.oz | 30ml</p>
    </section>

    <section class="label label--teal">
      <div class="label__top"></div>
      <div class="brand-badge"><span class="brand-name">QBTx</span></div>
      <div class="state-map" role="img" aria-label="Faint state outline map"></div>
      <h1 class="product-title">CBD OIL</h1>
      <p class="product-type">FULL SPECTRUM OIL</p>
      <p class="strength">500MG</p>
      <p class="flavor">Peppermint</p>
      <p class="spectrum">BROAD SPECTRUM</p>
      <p class="net-weight">Net wt. 1fl.oz | 30ml</p>
    </section>
  </main>
</body>
</html>
```